Stationery & Business Card Design Project

We require our stationary to be professional, which will stand out but also be sophisticated and reputable.

We also require the following:

* Business card must be double sided
* Logo must stand out with brightnest colours used. Other colours may be added but only in small doses as not to overtake the main colours.
* For business card brightnest pty ltd smsf specialists with administrators at bottom left on the front of the card and details on the back

Industry/Entity Type

Business

Requirements
Must have
• * Business Cards
* With compliments slips –2 different ones
* Forwarding mail slip (smaller version of a with compliments slip)

```html
<!DOCTYPE html>
<html lang="en">
<head>
<meta charset="utf-8">
<title>brightnest business card</title>
<link href="https://fonts.googleapis.com/css2?family=Source+Sans+3:wght@400;600;700&display=swap" rel="stylesheet">
<style>
  :root {
    --stage: #000000;
    --navy: #1f2266;
    --navy-deep: #14164a;
    --navy-light: #3a3f92;
    --grey: #8a8a8e;
    --grey-light: #d9d9dc;
    --ink: #6b6b70;
    --white: #ffffff;
  }
  * { margin: 0; padding: 0; box-sizing: border-box; }
  html, body {
    width: 1200px; height: 900px; overflow: hidden;
    background: var(--stage);
    font-family: "Source Sans 3", "Helvetica Neue", Arial, sans-serif;
  }
  .stage { position: relative; width: 1200px; height: 900px; }
  .card {
    position: absolute; top: 325px;
    width: 509px; height: 312px; overflow: hidden;
  }
  /* front */
  .card-front { left: 77px; background: var(--white); }
  .front-shape { position: absolute; inset: 0; }
  .brand-name {
    position: absolute; left: 34px; top: 26px;
    font-size: 46px; font-weight: 600; letter-spacing: -1.5px;
    color: var(--navy); line-height: 1;
  }
  .brand-tagline {
    position: absolute; left: 36px; top: 74px;
    font-size: 10px; font-weight: 700; letter-spacing: 3.2px;
    color: var(--navy); line-height: 1;
  }
  .person-name {
    position: absolute; left: 33px; top: 126px;
    font-size: 15px; font-weight: 700; color: var(--navy);
  }
  .person-title {
    position: absolute; left: 33px; top: 144px;
    font-size: 14px; color: var(--ink);
  }
  .contact-list {
    position: absolute; left: 30px; top: 196px; list-style: none;
  }
  .contact-list li {
    display: flex; align-items: center; gap: 7px;
    height: 17px; font-size: 12.5px; color: var(--ink);
  }
  .contact-list svg { width: 12px; height: 12px; fill: var(--navy); flex: none; }
  /* back */
  .card-back {
    left: 613px;
    background: radial-gradient(ellipse 70% 65% at 50% 30%, var(--navy-light) 0%, var(--navy) 55%, var(--navy-deep) 100%);
  }
  .back-shape { position: absolute; inset: 0; }
  .back-logo {
    position: absolute; left: 101px; top: 114px;
    display: flex; align-items: center; gap: 10px;
  }
  .logo-square {
    width: 78px; height: 78px; border-radius: 6px;
    background: var(--grey);
  }
  .back-brand { display: flex; flex-direction: column; }
  .back-brand .name {
    font-size: 42px; font-weight: 600; letter-spacing: -1.3px;
    color: var(--white); line-height: 1;
  }
  .back-brand .tagline {
    font-size: 9px; font-weight: 700; letter-spacing: 3px;
    color: var(--white); margin-top: 2px; margin-left: 2px;
  }
  .back-web {
    position: absolute; left: 0; right: 0; top: 284px;
    text-align: center; font-size: 15px; letter-spacing: 2px;
    color: var(--white);
  }
  .back-web strong { font-weight: 700; }
</style>
</head>
<body>
<main class="stage">

  <section class="card card-front">
    <svg class="front-shape" viewBox="0 0 509 312" width="509" height="312" aria-hidden="true">
      <path d="M430 0 Q340 190 240 312 L509 312 L509 0 Z" fill="var(--navy)"/>
      <path d="M430 0 Q340 190 240 312" fill="none" stroke="var(--grey-light)" stroke-width="14"/>
    </svg>
    <div class="brand-name">brightnest</div>
    <div class="brand-tagline">smsf specialists</div>
    <div class="person-name">Claire Moffat</div>
    <div class="person-title">Independent Distributor</div>
    <ul class="contact-list">
      <li><svg viewBox="0 0 12 12"><rect x="1" y="3" width="6" height="9"/><rect x="7" y="0" width="4" height="12"/></svg>PO Box 318, Winnellie, NT 0821</li>
      <li><svg viewBox="0 0 12 12"><path d="M0 2h12v8H0z M1 3l5 4 5-4" fill="none" stroke="var(--navy)" stroke-width="1.3"/></svg>claire@brightnest.com.au</li>
      <li><svg viewBox="0 0 12 12"><rect x="3" y="0" width="6" height="12" rx="1"/></svg>0413 682 507</li>
      <li><svg viewBox="0 0 12 12"><path d="M0 5c0-3 12-3 12 0v1H9V4H3v2H0z"/><rect x="2" y="7" width="8" height="5" rx="1"/></svg>1300 486 2719</li>
      <li><svg viewBox="0 0 12 12"><circle cx="6" cy="6" r="5.5"/><path d="M0.5 6h11 M6 0.5v11" stroke="var(--white)" stroke-width="0.9"/></svg>www.brightnest.com.au</li>
    </ul>
  </section>

  <section class="card card-back">
    <svg class="back-shape" viewBox="0 0 509 312" width="509" height="312" aria-hidden="true">
      <path d="M0 0 L509 0 L509 70 Q260 150 0 115 Z" fill="var(--white)" opacity="0.06"/>
    </svg>
    <div class="back-logo">
      <div class="logo-square"></div>
      <div class="back-brand">
        <span class="name">brightnest</span>
        <span class="tagline">smsf specialists</span>
      </div>
    </div>
    <div class="back-web">www.<strong>brightnest</strong>.com.au</div>
  </section>

</main>
</body>
</html>
```